Venture Capital firm needs modern business cards

We are a Venture Capital firm within financial services/Asset management. The industry generally has basic business cards with black, blue and maybe green/yellow design elements.
Our firm has a four-colour swoosh logo. We are based in London and want to stand out, just a little bit!, from the crowd. Our company is called ROLK Investments and the 'C' stands for collaboration thus using artfolkhub is a natural portal for our business card design competition. Our logo came via artfolkhub too!
We use 'Venture Partner in Asset Management' as our tagline and this is Trademark registered. We operate in a conservative industry and we should not overstep our mark. The logo is colorful as it is and therefore the rest of the design should not be too fanciful.
The objective is twofold: make our logo element stick and memorable with our audience, whilst representing a conservative yet young image.
The Business Card obviously needs a field for Name, Surname, Job Title, Adress fields: Street, City, Postcode, Country, telefone and cell number, website address, etc.
We have uploaded the ai file. We trust that these are OK. If not, please advise.
Reason: We have have been busy with a client engagement. We will set the project as Guaranteed in return for the troubles we cause. Apologies for the confusion.
Thank you all for these great and creative design suggestions. The team is very happy with a number of your ideas! We will be in touch tomorrow to give individual feedback before the project closes on Friday. We look forward to working with some of you to narrow down your creations. Thank you, ROLK Investments team.
All,
Target Market(s)
Financial Services Professionals, Investors, Media, 35-70 years, mainly male, well educated
Industry/Entity Type
Conservative
Requirements
Must have
- We must make use of our logo and potential tagline 'Venture Partner in Asset Management' as we are establishing a new Brand and new company in the market.
We can use 'ROLK', 'ROLK Investments', and 'ROLK Investments'+tagline 'Venture Partner in Asset Management' or simply the four-colour swoosh plus the name of the company as part of the text. (see files)
All design elements are available in black or grey-scale if required. (grey scale swoosh attached).
Due to regulation we must have the following wording on the card in small print 'ROLK Investments is an Appointed Representative of Brambury Monetary Ventures Limited, which is authorised by the Pemberton Oversight Board'.
Nice to have
- We would consider designs that make use of different printing techniques such embossing/debossing, UV spot etc.
We attach our colour palette in the files section for your reference.
Should not have
- The font we use for our company name is 'EXO' so do not use a font style that clashes with the corporate fonts, please.
Do not use other design elements than the ones we provide in the file library as part of this project.

```html
<!DOCTYPE html>
<html lang="en">
<head>
<meta charset="utf-8">
<title>ROLK Investments – Business Card</title>
<link rel="stylesheet" href="https://fonts.googleapis.com/css2?family=Exo:wght@300;400;500&display=swap">
<style>
  :root {
    --backdrop: #3b3b3c;
    --card: #ffffff;
    --pattern-light: #f4f4f4;
    --pattern-dark: #e6e6e6;
    --ink: #3a3a3c;
    --ink-soft: #6b6b6e;
    --accent: #7d1f5f;
    --rule: #8a8a8a;
  }
  * { box-sizing: border-box; margin: 0; padding: 0; }
  html, body {
    width: 1200px; height: 901px; overflow: hidden;
    background: var(--backdrop);
    font-family: "Exo", sans-serif;
    color: var(--ink);
  }
  .stage {
    position: relative; width: 1200px; height: 901px;
    display: flex; align-items: center; justify-content: center; gap: 60px;
  }
  .card {
    position: relative; width: 520px; height: 300px;
    background: var(--card);
    box-shadow: 0 14px 30px rgba(0,0,0,.45);
    overflow: hidden;
  }

  /* Front */
  .card-front .pattern {
    position: absolute; inset: 0;
    background: radial-gradient(ellipse at center, var(--card) 0%, var(--card) 30%, var(--pattern-light) 60%, var(--pattern-dark) 100%);
  }
  .card-front .brand-block { position: absolute; left: 120px; top: 110px; }
  .brand-row { display: flex; align-items: center; gap: 12px; }
  .brand-dot {
    width: 34px; height: 34px; border-radius: 50%;
    background: var(--accent); flex: none;
  }
  .brand-name {
    font-weight: 400; font-size: 50px; line-height: 1;
    color: var(--ink); letter-spacing: 1px;
  }
  .tagline {
    margin-top: 6px; margin-left: 46px;
    font-size: 9px; font-weight: 400; color: var(--ink-soft);
  }

  /* Back */
  .card-back .brand-block { position: absolute; left: 40px; top: 70px; }
  .card-back .brand-dot { width: 28px; height: 28px; }
  .card-back .brand-name { font-size: 44px; }
  .brand-sub {
    margin-left: 42px; margin-top: 2px;
    font-size: 11px; font-weight: 400; letter-spacing: 4px;
    color: var(--ink);
  }
  .contact { position: absolute; left: 300px; top: 36px; }
  .person-name { font-size: 19px; font-weight: 400; color: var(--accent); line-height: 1.25; }
  .person-title { font-size: 12px; font-weight: 300; color: var(--ink-soft); margin-bottom: 10px; }
  .contact-list { list-style: none; font-size: 12px; font-weight: 300; line-height: 1.45; }
  .contact-list .label { color: var(--accent); display: inline-block; width: 14px; }
  .address {
    position: absolute; left: 300px; top: 150px;
    font-size: 12px; font-weight: 300; line-height: 1.45; font-style: normal;
  }
  .disclaimer {
    position: absolute; left: 40px; right: 28px; top: 212px;
    font-size: 9.5px; line-height: 1.45; font-weight: 300; color: var(--ink);
    text-align: right;
  }
  .disclaimer-rule {
    position: absolute; left: 40px; right: 28px; top: 246px;
    height: 1px; background: var(--rule);
  }
</style>
</head>
<body>
<main class="stage">
  <section class="card card-front" aria-label="Business card front">
    <div class="pattern" role="img" aria-label="Faint grey repeating brand swirl pattern"></div>
    <div class="brand-block">
      <div class="brand-row">
        <span class="brand-dot"></span>
        <span class="brand-name">ROLK</span>
      </div>
      <p class="tagline">Venture Partner in Asset Management</p>
    </div>
  </section>

  <section class="card card-back" aria-label="Business card back">
    <div class="brand-block">
      <div class="brand-row">
        <span class="brand-dot"></span>
        <span class="brand-name">ROLK</span>
      </div>
      <p class="brand-sub">Investments</p>
    </div>

    <div class="contact">
      <h1 class="person-name">Marcus Hellworth</h1>
      <p class="person-title">managing director</p>
      <ul class="contact-list">
        <li><span class="label">p</span> 020 7946 0312</li>
        <li><span class="label">c</span> 07700 900 418</li>
        <li><span class="label">e</span> info@rolkinvestment.com</li>
      </ul>
    </div>
    <address class="address">
      47 Harrow Lane<br>
      Eastbridge, New York 10482<br>
      www.rolkinvestment.com
    </address>

    <p class="disclaimer">ROLK Investments is an Appointed Representative of Brambury Monetary Ventures Limited,<br>which is authorised by the Pemberton Oversight Board</p>
    <div class="disclaimer-rule"></div>
  </section>
</main>
</body>
</html>
```